A simple Chatterbook Ad (not Chatterbook Page) for weight loss surgery

It’s a simple ad in terms of the text.

The text should say:
Curious about weight loss surgery?
This 30 second quiz will tell you which procedure will suit you best

I'm open to variations in the text if it is thought to enhance the ad.

Targeted towards obese individuals who have been unable to lose weight with diet and exercise. My industry is weight loss surgery – webpage www.marcusbellweather.com.au. Clicking the ad leads to a quiz on my webpage relating to weight loss surgery. Most frequent users of this service are females (75%) between ages of 35 and 55 years.

Successful weight loss surgery can enable individuals who have been unable to lose weight to lose a substantial amount of the excess weight they are carrying to be healthier and happier.

```html
<!DOCTYPE html>
<html lang="en">
<head>
<meta charset="utf-8">
<title>Weight Loss Surgery Quiz Ad</title>
<link rel="stylesheet" href="https://fonts.googleapis.com/css2?family=Playfair+Display:wght@400&family=Jost:wght@400&display=swap">
<style>
  :root {
    --teal: #1ba89b;
    --ink: #2b2b2b;
    --grey: #8a8f92;
    --paper: #ffffff;
    --photo-top: #f1efee;
    --photo-bottom: #ddd8d6;
  }
  html, body {
    margin: 0;
    padding: 0;
    width: 1200px;
    height: 1200px;
    overflow: hidden;
    background: var(--paper);
  }
  .ad {
    position: relative;
    width: 1200px;
    height: 1200px;
    background: var(--paper);
    overflow: hidden;
  }
  .headline {
    position: absolute;
    left: 76px;
    top: 82px;
    margin: 0;
    font-family: "Playfair Display", serif;
    font-weight: 400;
    font-size: 160px;
    line-height: 158px;
    letter-spacing: -3px;
    color: var(--teal);
    white-space: nowrap;
  }
  .subline {
    position: absolute;
    left: 80px;
    top: 625px;
    margin: 0;
    font-family: "Jost", sans-serif;
    font-weight: 400;
    font-size: 56px;
    line-height: 75px;
    color: var(--ink);
    white-space: nowrap;
  }
  .scale-photo {
    position: absolute;
    left: 560px;
    top: 766px;
    width: 640px;
    height: 434px;
    border-radius: 60px 0 0 0;
    background: linear-gradient(180deg, var(--photo-top) 0%, var(--photo-bottom) 100%);
  }
  .brand {
    position: absolute;
    left: 84px;
    top: 1052px;
    display: flex;
    align-items: center;
    gap: 16px;
  }
  .brand-dot {
    width: 70px;
    height: 70px;
    border-radius: 50%;
    background: var(--teal);
  }
  .brand-name {
    font-family: "Playfair Display", serif;
    font-size: 33px;
    line-height: 1;
    letter-spacing: 0.5px;
    text-transform: uppercase;
    color: var(--teal);
    white-space: nowrap;
  }
  .brand-role {
    margin-top: 6px;
    font-family: "Playfair Display", serif;
    font-size: 14px;
    letter-spacing: 1.5px;
    color: var(--grey);
    white-space: nowrap;
  }
</style>
</head>
<body>
  <main class="ad">
    <h1 class="headline">Curious about<br>weight loss<br>surgery?</h1>
    <p class="subline">This 30 second quiz will<br>tell you which procedure<br>will suit you best</p>
    <div class="scale-photo" role="img" aria-label="Photo of bare feet standing on a white bathroom scale whose display reads HELP!"></div>
    <div class="brand">
      <span class="brand-dot"></span>
      <div>
        <div class="brand-name">Marcus Bellweather</div>
        <div class="brand-role">General, Upper GI &amp; Bariatric Surgeon</div>
      </div>
    </div>
  </main>
</body>
</html>
```